Poster design for the WILLOW WISP magic show.

We need a poster design for our magic show. This isn't your typical 'small town' magic show. Our show features world class magicians from the Velvet Lantern, in Hollywood California. The show is geared toward everyone, it is family friendly - with a little bit of an edge. We want people to see the poster and feel like they are going to have a unique and sophisticated magical experience. We also want individuals and couples to see the poster and feel like it is a show for them and not only for children.
Updates

Target Market(s)

BRT audience, family audience, the age range is anywhere from 5 - 105. Cool people.

Industry/Entity Type

Town

Requirements
Must have
• Our attached .jpg of the magician floating in the air. Poster size 24x36"
Must have text:
The 3rd Annual Albuquerque Conjuring Gala Presents (small type)
Willow Wisp (should be larger type)
November 24th - 25th
Showtimes 3:00PM & 7:30PM Saturday, 2:00PM Sunday
Tickets available at www.DorvaSeats.example For more information contact Dorva Theatre @ 505.555.0147
Nice to have
• A sort of old school/antique feeling to the poster.
Perhaps a theater marquee
Check out www.grovelumen.example - we love the feeling of this site for our poster...
Feel free to adjust the provided .jpg accordingly in regards to color/size/interaction with the rest of the poster
Should not have
• Should not have clowns, bunnies, anything that would make it feel like a 3 year old's magic themed birthday party.

```html
<!DOCTYPE html>
<html lang="en">
<head>
<meta charset="utf-8">
<title>Willow Wisp — Poster</title>
<link rel="stylesheet" href="https://fonts.googleapis.com/css2?family=Alfa+Slab+One&family=Archivo+Black&family=Archivo:wght@700;800&display=swap">
<style>
  :root {
    --ink: #0b0b0b;
    --paper: #ffffff;
    --gold-light: #fff3b0;
    --gold: #f2b21c;
    --gold-deep: #b9730a;
    --bronze: #6b3e10;
    --stage-red: #8e1c12;
    --stage-dark: #3a0a06;
    --bulb-white: #fffbe6;
    --bulb-warm: #ffd27a;
    --bulb-amber: #e8962e;
    --ceiling: #3a2414;
    --facade: #2e231b;
    --pavement: #8d8a86;
    --footer-ink: #1a1a1a;
  }
  * { margin: 0; padding: 0; box-sizing: border-box; }
  html, body { width: 800px; height: 1200px; overflow: hidden; background: #222; }
  .poster {
    position: relative;
    width: 800px;
    height: 1200px;
    overflow: hidden;
    font-family: "Archivo", Arial, sans-serif;
    background: linear-gradient(180deg, var(--facade) 0%, #3f3a35 70%, var(--pavement) 100%);
  }
  .marquee-lights {
    position: absolute;
    left: 0; top: 330px;
    width: 800px; height: 290px;
    background:
      radial-gradient(ellipse 55% 22% at 70% 48%, rgba(255,251,230,.95), rgba(255,210,122,.6) 45%, transparent 80%),
      radial-gradient(ellipse 50% 20% at 28% 70%, rgba(255,251,230,.9), rgba(255,210,122,.55) 45%, transparent 80%),
      radial-gradient(ellipse 40% 16% at 92% 30%, rgba(255,251,230,.85), rgba(255,210,122,.5) 50%, transparent 80%),
      linear-gradient(180deg, var(--bulb-amber) 0%, #c9701f 35%, #a2561a 60%, var(--ceiling) 88%, var(--facade) 100%);
  }
  .facade-photo {
    position: absolute;
    left: 0; top: 620px;
    width: 800px; height: 580px;
    background: linear-gradient(180deg, var(--facade) 0%, #3f3a35 55%, #8a8783 100%);
  }
  .header-band { position: absolute; left: 0; top: 0; width: 800px; height: 500px; }
  .kicker {
    position: absolute; left: 0; width: 800px; text-align: center;
    color: var(--paper); font-weight: 800;
  }
  .kicker--event { top: 112px; font-size: 28px; }
  .kicker--presents { top: 152px; font-size: 32px; }
  .ornament {
    position: absolute;
    background: radial-gradient(ellipse at center, rgba(242,178,28,.75), rgba(185,115,10,.35) 55%, transparent 75%);
  }
  .ornament--top { left: 220px; top: 20px; width: 360px; height: 50px; }
  .ornament--left { left: 0; top: 0; width: 120px; height: 90px; }
  .ornament--right { right: 0; top: 0; width: 120px; height: 90px; }
  .tilted {
    position: absolute; left: 0; top: 0; width: 800px; height: 500px;
    transform-origin: 400px 330px;
    transform: rotate(-7deg);
  }
  .show-title {
    position: absolute; left: 0; top: 236px; width: 800px; text-align: center;
    font-family: "Alfa Slab One", Georgia, serif;
    font-weight: 400;
    font-size: 110px; line-height: 1;
    color: var(--gold);
    background: linear-gradient(180deg, var(--gold-light) 0%, var(--gold) 45%, var(--gold-deep) 100%);
    -webkit-background-clip: text; background-clip: text;
    -webkit-text-fill-color: transparent;
    filter: drop-shadow(2px 2px 0 #000) drop-shadow(2px 2px 0 #000) drop-shadow(2px 2px 0 #111) drop-shadow(1px 1px 0 #222);
  }
  .show-dates {
    position: absolute; left: 0; top: 352px; width: 800px; text-align: center;
    font-family: "Archivo Black", Arial, sans-serif;
    font-size: 38px; line-height: 1; color: var(--ink);
  }
  .showtimes {
    position: absolute; left: 0; top: 402px; width: 800px; text-align: center;
    font-family: "Archivo Black", Arial, sans-serif;
    font-size: 21px; line-height: 1; color: var(--ink);
  }
  .stage {
    position: absolute; left: 52px; top: 607px; width: 700px; height: 473px;
  }
  .stage-photo {
    position: absolute; inset: 12px;
    background:
      radial-gradient(ellipse 60% 40% at 50% 10%, rgba(255,180,90,.7), transparent 70%),
      radial-gradient(ellipse 80% 70% at 50% 45%, #c23a1e, var(--stage-red) 50%, var(--stage-dark) 100%);
  }
  .stage-frame {
    position: absolute; inset: 0;
    border: 4px solid var(--gold);
    outline: 2px solid var(--bronze);
    outline-offset: -10px;
    box-shadow: 0 0 18px rgba(0,0,0,.7);
  }
  .ticket-info {
    position: absolute; left: 0; top: 1124px; width: 800px; text-align: center;
    color: var(--footer-ink); line-height: 1.12;
  }
  .ticket-info__url { font-family: "Archivo Black", Arial, sans-serif; font-size: 22px; }
  .ticket-info__contact { font-size: 19px; font-weight: 800; }
  .ticket-info__phone { font-family: "Archivo Black", Arial, sans-serif; font-size: 26px; }
</style>
</head>
<body>
<main class="poster">
  <div class="marquee-lights" role="img" aria-label="Theatre marquee ceiling lined with rows of glowing bulbs"></div>
  <div class="facade-photo" role="img" aria-label="Theatre front and pavement beneath the marquee"></div>

  <svg class="header-band" viewBox="0 0 800 500" aria-hidden="true">
    <polygon points="0,0 800,0 800,213 0,357" fill="var(--ink)"/>
    <polygon points="0,357 800,213 800,386 0,482" fill="var(--paper)"/>
  </svg>

  <div class="ornament ornament--top" role="img" aria-label="Gold scrollwork flourish"></div>
  <div class="ornament ornament--left" role="img" aria-label="Gold corner scrollwork"></div>
  <div class="ornament ornament--right" role="img" aria-label="Gold corner scrollwork"></div>

  <p class="kicker kicker--event">The 3rd Annual Albuquerque Conjuring Gala</p>
  <p class="kicker kicker--presents">~ Presents ~</p>

  <div class="tilted">
    <h1 class="show-title">Willow Wisp</h1>
    <p class="show-dates">November 24th - 25th</p>
    <p class="showtimes">Showtimes: 3:00 pm &amp; 7:30 pm, Saturday • 2:00 pm, Sunday</p>
  </div>

  <figure class="stage">
    <div class="stage-photo" role="img" aria-label="Magician floating mid-air beside a chair on a red-lit stage"></div>
    <div class="stage-frame"></div>
  </figure>

  <footer class="ticket-info">
    <p class="ticket-info__url">Tickets available at www.DorvaSeats.example</p>
    <p class="ticket-info__contact">For more information contact Dorva Theatre</p>
    <p class="ticket-info__phone">505.555.0147</p>
  </footer>
</main>
</body>
</html>
```